The Cellar Academy - Flyer Design Project

I need a flyer to be posted in culinary schools and universities to promote my wine education classes.

These are the points to make on the flyer:

> for the first time in your area - the Grape & Cask Learning Council
> world class wine and spirits education - courses designed for business
> enhance your wine qualifications - online with GCLC's new distance learning program
> expand your culinary degree - with wine credentials that get you to the head of the class
> Sign-up now at TheCellarACD.com or call 555.204.3378

CALL TO ACTION is "Mention this offer, receive 10% discount"

These are logos and graphics you can use:
https://www.filecourierhub.com/download/Xk4pQm7rTz2LwN9aBv
https://www.filecourierhub.com/download/Xk4pQm7rTz8HdR3cYe
https://www.filecourierhub.com/download/Xk4pQm7rJu5VsK1fGh
https://www.filecourierhub.com/download/Xk4pQm7rPo6WmE4jLq

Industry/Entity Type

Education

Requirements
Must have
• Use our webiste to get a look and feel (thecellaracd.com). We like simple and elegant. No need to clutter the flyer with wine bottles, grapes and glasses. The focus is on World Class Wine Education that can help students get jobs.

```html
<!DOCTYPE html>
<html lang="en">
<head>
<meta charset="utf-8">
<title>The Cellar Academy – Wine Education Flyer</title>
<link rel="stylesheet" href="https://fonts.googleapis.com/css2?family=Oswald:wght@400;600;700&display=swap">
<style>
  :root {
    --band-rose: #b46a6f;
    --band-rose-dark: #a55a60;
    --photo-deep: #1a0708;
    --photo-wine: #5a1a1e;
    --photo-glow: #8a3a3c;
    --circle-veil: rgba(246, 232, 231, 0.86);
    --headline-red: #a3221d;
    --subline-dark: #3d1214;
    --offer-band: #7a1b1e;
    --offer-text: #ffffff;
    --logo-white: #ffffff;
  }
  * { margin: 0; padding: 0; box-sizing: border-box; }
  html, body { width: 849px; height: 1200px; overflow: hidden; background: #ffffff; }
  .flyer {
    position: relative;
    width: 849px;
    height: 1200px;
    overflow: hidden;
    font-family: "Oswald", "Arial Narrow", sans-serif;
    background: var(--photo-deep);
  }
  .top-band {
    position: absolute;
    left: 0; top: 0;
    width: 849px; height: 186px;
    background: linear-gradient(180deg, var(--band-rose) 0%, var(--band-rose-dark) 100%);
  }
  .brand-name {
    position: absolute;
    left: 300px; top: 40px;
    width: 250px;
    color: var(--logo-white);
    font-weight: 400;
    font-size: 44px;
    line-height: 1.05;
    letter-spacing: 1px;
  }
  .hero-photo {
    position: absolute;
    left: 0; top: 186px;
    width: 849px; height: 1014px;
    background:
      radial-gradient(ellipse 280px 360px at 340px 300px, var(--photo-glow) 0%, rgba(138,58,60,0) 70%),
      radial-gradient(ellipse 140px 520px at 700px 440px, var(--photo-wine) 0%, rgba(90,26,30,0) 80%),
      linear-gradient(160deg, var(--photo-wine) 0%, var(--photo-deep) 60%, #0e0405 100%);
  }
  .message-circle {
    position: absolute;
    left: 100px; top: 612px;
    width: 650px; height: 650px;
    border-radius: 50%;
    background: var(--circle-veil);
  }
  .message {
    position: absolute;
    left: 0; top: 715px;
    width: 849px;
    text-align: center;
    text-transform: uppercase;
  }
  .point { margin-bottom: 14px; }
  .headline {
    color: var(--headline-red);
    font-weight: 700;
    font-size: 25px;
    line-height: 1.12;
    letter-spacing: 0.6px;
  }
  .subline {
    color: var(--subline-dark);
    font-weight: 600;
    font-size: 15px;
    line-height: 1.4;
    letter-spacing: 0.5px;
  }
  .signup { margin-top: 22px; }
  .offer {
    display: inline-block;
    margin-top: 18px;
    padding: 7px 22px;
    background: var(--offer-band);
    color: var(--offer-text);
    font-weight: 600;
    font-size: 17px;
    letter-spacing: 0.8px;
  }
</style>
</head>
<body>
  <div class="flyer">
    <div class="hero-photo" role="img" aria-label="Dark, moody photograph of a red wine glass beside a wine bottle"></div>
    <header class="top-band">
      <div class="brand-name">The Cellar Academy</div>
    </header>
    <div class="message-circle"></div>
    <main class="message">
      <div class="point">
        <p class="headline">For the first time in your area</p>
        <p class="subline">The Grape &amp; Cask Learning Council</p>
      </div>
      <div class="point">
        <p class="headline">World class wine &amp; spirits education</p>
        <p class="subline">Courses designed for business</p>
      </div>
      <div class="point">
        <p class="headline">Enhance your wine qualifications</p>
        <p class="subline">Online with GCLC's new distance<br>learning program</p>
      </div>
      <div class="point">
        <p class="headline">Expand your culinary degree</p>
        <p class="subline">With wine credentials that get you<br>to the head of the class</p>
      </div>
      <div class="signup">
        <p class="headline">Sign up now at TheCellarACD.com</p>
        <p class="headline">or call 555.204.3378</p>
      </div>
      <p class="offer">Mention this offer, receive 10% discount</p>
    </main>
  </div>
</body>
</html>
```